brevity cafe flyer design project

A funky trendy cafe in Melbourne’s CBD that caters too a large range of corporate clients. Located on the door step of a major train station, its a quick turn around cafe for the short time frame customer but also a cafe to sit, relax and enjoy the hustle and bustle from the inside out. We provide All day breakfast, gourmet sandwiches, gourmet rotti wraps, a la carte menu and also heat and serve meals.

BREAKFAST TO GO! ALL BREAKFAST TO GO ITEMS COME WITH A MEDIUM TAKE AWAY COFFEE!
• RAISIN TOAST & COFFEE – $6
• BACON & EGG MUFFIN & COFFEE $7.5
• SPINACH, MUSHROOM OMELETTE MUFFIN & COFFEE $7.5
• OMELETTE WITH CHEESE MUFFIN & COFFEE $7.5
• HAM & CHEESE CROISSANT & COFFEE $7.5
• SWEET OR SAVOURY MUFFIN & COFFEE $6.5
• HAM & CHEESE SANDWICH & COFFEE $8.0
• HAM, CHEESE & TOMATO SANDWICH & COFFEE $8.5

*NOT IN CONJUNCTION WITH BREVITY CLUB CARD OFFER

WE ALSO HAVE PRE-MADE LUNCH OPTIONS – ASSORTED ROTTI WRAPS (Bbq chicken, honey mustard chicken, pesto chicken & vegetarian) ASSORTED GOURMET SANDWICHES (Mediterranean, Moroccan chicken, Salami, Chicken Schnitzel, Salmon, Brevity & Roast Beef) Soup of the day Pasta of the day Salad of the day

Ph- 03 9718 4630 Fax- 03 9718 4637 Web – www.brevitycafe.com.au 182 DORNAL STREET MELBOURNE 3000

Industry/Entity Type

Cafe

Font styles to use
Serif

Requirements
Must have
• Our 2 branded colours -

PMS 392c
PMS BLACK

```html
<!DOCTYPE html>
<html lang="en">
<head>
<meta charset="utf-8">
<title>Brevity Cafe – Breakfast to Go Flyer</title>
<link href="https://fonts.googleapis.com/css2?family=Comfortaa:wght@500;700&family=Arimo:wght@400;700&family=Gochi+Hand&display=swap" rel="stylesheet">
<style>
  :root{
    --lime:#c6dc1c;
    --black:#0b0b0b;
    --panel:#1b1b1b;
    --banner:#262626;
    --white:#f2f2f2;
    --page:#d9d9d9;
  }
  *{margin:0;padding:0;box-sizing:border-box}
  html,body{width:831px;height:1200px;overflow:hidden;background:var(--page)}
  .flyer{
    position:absolute;left:146px;top:40px;width:540px;height:1120px;
    background:var(--black);overflow:hidden;
    font-family:"Arimo",Arial,sans-serif;color:var(--lime);
  }
  .flyer-top{
    position:absolute;left:0;top:0;width:100%;height:250px;
    background:linear-gradient(180deg,#161616 0%,#1c1c1c 70%,#0b0b0b 100%);
  }
  .logo-banner{position:absolute;left:150px;top:0;width:240px;height:215px}
  .brand-name{
    position:absolute;left:0;top:118px;width:240px;text-align:center;
    font-family:"Comfortaa",sans-serif;font-weight:700;font-size:22px;letter-spacing:2px;color:var(--lime);
  }
  .brand-dot{
    position:absolute;left:104px;top:56px;width:32px;height:32px;border-radius:50%;background:var(--lime);
  }
  .headline{position:absolute;left:0;top:250px;width:100%;height:200px;font-family:"Comfortaa",sans-serif;font-weight:700}
  .headline .word-breakfast{position:absolute;left:70px;top:12px;font-size:58px;letter-spacing:-1px}
  .headline .word-to{position:absolute;left:112px;top:92px;font-size:28px}
  .headline .word-go{position:absolute;left:162px;top:62px;font-size:120px;line-height:1;letter-spacing:-4px}
  .headline .bang{position:absolute;left:400px;top:-80px;font-size:220px;line-height:1}
  .offer{position:absolute;left:60px;top:470px;width:360px;text-align:right;font-family:"Gochi Hand",cursive;color:var(--white)}
  .offer-main{font-size:25px;letter-spacing:.5px}
  .offer-sub{font-size:17px;letter-spacing:.5px}
  .cup{position:absolute;left:428px;top:446px;width:56px;height:84px;border-radius:6px 6px 12px 12px;
    background:linear-gradient(180deg,#d6e84a 0%,#1c1c1c 30%,#111 100%)}
  .brush-lime{position:absolute;left:60px;top:540px}
  .menu{position:absolute;left:60px;top:560px;width:420px;list-style:none;font-size:13.5px;letter-spacing:.2px}
  .menu li{display:flex;align-items:baseline;height:20px}
  .menu .item{white-space:nowrap}
  .menu .leader{flex:1;border-bottom:1.5px dotted var(--white);margin:0 4px;transform:translateY(-3px)}
  .menu .price{color:var(--white)}
  .brush-white{position:absolute;left:50px;top:766px}
  .disclaimer{position:absolute;left:60px;top:786px;font-size:12px;color:var(--white);letter-spacing:.5px}
  .lime-band{position:absolute;left:0;top:852px;width:100%;height:10px;background:var(--lime)}
  .contact-row{position:absolute;left:20px;top:880px;display:flex;align-items:center;gap:8px;
    font-family:"Comfortaa",sans-serif;font-weight:700;font-size:21px}
  .contact-row .label{color:var(--lime)}
  .contact-row .number{background:var(--lime);color:var(--black);padding:3px 8px}
  .contact-row .bar{width:8px;height:30px;background:var(--lime)}
  .web{position:absolute;left:40px;top:955px;font-family:"Comfortaa",sans-serif;font-weight:700;font-size:30px}
  .address{position:absolute;left:40px;top:1010px;font-family:"Comfortaa",sans-serif;font-weight:700;font-size:17px;letter-spacing:.5px}
</style>
</head>
<body>
<main class="flyer">
  <div class="flyer-top"></div>

  <div class="logo-banner">
    <svg width="240" height="215" viewBox="0 0 240 215" aria-hidden="true">
      <polygon points="0,0 240,0 240,180 120,215 0,180" fill="var(--banner)"/>
    </svg>
    <span class="brand-dot"></span>
    <div class="brand-name">BREVITY CAFE</div>
  </div>

  <h1 class="headline">
    <span class="word-breakfast">BREAKFAST</span>
    <span class="word-to">to</span>
    <span class="word-go">GO</span>
    <span class="bang">!</span>
  </h1>

  <div class="offer">
    <p class="offer-main">ALL BREAKFAST TO GO ITEMS</p>
    <p class="offer-sub">COME WITH A MEDIUM TAKE AWAY COFFEE!</p>
  </div>
  <div class="cup" role="img" aria-label="Take away coffee cup"></div>

  <svg class="brush-lime" width="420" height="10" viewBox="0 0 420 10" aria-hidden="true">
    <path d="M0 8 L420 1 L420 4 L2 10 Z" fill="var(--lime)"/>
  </svg>

  <ul class="menu">
    <li><span class="item">RAISIN TOAST &amp; COFFEE</span><span class="leader"></span><span class="price">$6</span></li>
    <li><span class="item">BACON &amp; EGG MUFFIN &amp; COFFEE</span><span class="leader"></span><span class="price">$7.5</span></li>
    <li><span class="item">SPINACH, MUSHROOM OMELETTE MUFFIN &amp; COFFEE</span><span class="leader"></span><span class="price">$7.5</span></li>
    <li><span class="item">OMELETTE WITH CHEESE MUFFIN &amp; COFFEE</span><span class="leader"></span><span class="price">$7.5</span></li>
    <li><span class="item">HAM &amp; CHEESE CROISSANT &amp; COFFEE</span><span class="leader"></span><span class="price">$7.5</span></li>
    <li><span class="item">SWEET OR SAVOURY MUFFIN &amp; COFFEE</span><span class="leader"></span><span class="price">$6.5</span></li>
    <li><span class="item">HAM &amp; CHEESE SANDWICH &amp; COFFEE</span><span class="leader"></span><span class="price">$8.0</span></li>
    <li><span class="item">HAM &amp; CHEESE &amp; TOMATO SANDWICH &amp; COFFEE</span><span class="leader"></span><span class="price">$8.5</span></li>
  </ul>

  <svg class="brush-white" width="440" height="10" viewBox="0 0 440 10" aria-hidden="true">
    <path d="M0 8 L440 1 L440 3.5 L2 10 Z" fill="var(--white)"/>
  </svg>
  <p class="disclaimer">NOT IN CONJUNCTION WITH BREVITY CLUB CARD OFFER</p>

  <div class="lime-band"></div>
  <div class="contact-row">
    <span class="bar"></span>
    <span class="label">PHO</span><span class="number">03 9718 4630</span>
    <span class="label">FAX</span><span class="number">03 9718 4637</span>
  </div>
  <p class="web">www.BrevityCafe.com.au</p>
  <p class="address">182 DORNAL STREET MELBOURNE 3000</p>
</main>
</body>
</html>
```